Professional University Report Template

I have the need for a professionally-designed, multi-page report template, consisting of 8.5 x 11 inch pages - like a book, but not facing page design. An InDesign template would be best for my purposes.

This is a professional document in which I will need a main column for text, and a side column (around 1/3 of the width) to include photos, graphics, quotes, and lists. No background colors should be used, but perhaps some shading would be fine. This will be distributed as a PDF and will be printed by many in greyscale - so it should look great, and be easy to view without color.

As it is for a university publication, it must be overall professional and a bit subdued. The design should not overshadow the content, but enhance the overall experience. Most of all, I am aiming for something that is original and interesting.

Target Market(s)

University professors

Industry/Entity Type

University

Requirements
Must have
• Title page

Then a 3-page example document (use the text from sample indicator doc file):
Header 1 text
Header 2 text
body text
bulleted list
footer text noting the chapter title and page number

In the side columns of example pages (use the image files):
Photos
graphs
quoted text
bulleted list
Should not have
• No need for table of contents page, logo placement, or headers

```html
<!DOCTYPE html>
<html lang="en">
<head>
<meta charset="utf-8">
<title>Notable indicator 2: Enhancing courses through service-learning</title>
<link rel="stylesheet" href="https://fonts.googleapis.com/css2?family=Arimo:ital,wght@0,400;0,700;1,400;1,700&display=swap">
<style>
  :root {
    --page: #ffffff;
    --sidebar: #e3e3e3;
    --ink: #111111;
    --rule: #111111;
    --photo-top: #c9c2b4;
    --photo-bottom: #6f7f8c;
    --photo-frame: #ffffff;
  }
  * { margin: 0; padding: 0; box-sizing: border-box; }
  html, body { width: 927px; height: 1200px; overflow: hidden; background: var(--page); }
  .page {
    position: relative;
    width: 927px;
    height: 1200px;
    overflow: hidden;
    background: var(--page);
    color: var(--ink);
    font-family: "Arimo", Arial, sans-serif;
  }
  .line { display: block; white-space: nowrap; }
  .sidebar {
    position: absolute;
    left: 0; top: 0;
    width: 272px; height: 1200px;
    background: var(--sidebar);
  }
  .sidebar-photo {
    position: absolute;
    left: -8px; top: 200px;
    width: 312px; height: 218px;
    background: linear-gradient(170deg, var(--photo-top) 0%, #a8a89e 45%, var(--photo-bottom) 100%);
    border: 3px solid var(--photo-frame);
    transform: rotate(-7deg);
    box-shadow: 0 1px 3px rgba(0,0,0,0.25);
  }
  .pull-quote {
    position: absolute;
    left: 22px; top: 752px;
    width: 240px;
    font-size: 23.5px;
    line-height: 29.9px;
    font-weight: 700;
    font-style: italic;
  }
  .page-header {
    position: absolute;
    left: 318px; top: 66px;
    width: 572px;
    text-align: center;
    padding-bottom: 6px;
    border-bottom: 3px solid var(--rule);
  }
  .page-title {
    font-size: 44px;
    line-height: 46px;
    font-weight: 700;
    font-style: italic;
  }
  .page-subtitle {
    font-size: 19.5px;
    line-height: 22px;
    font-weight: 700;
    font-style: italic;
  }
  .main-column {
    position: absolute;
    left: 318px; top: 166px;
    width: 574px;
  }
  .section-heading {
    font-size: 23px;
    line-height: 28.6px;
    font-weight: 700;
    margin-bottom: 23px;
  }
  .body-text {
    font-size: 21.6px;
    line-height: 25.6px;
    margin-bottom: 34px;
  }
  .page-footer {
    position: absolute;
    left: 626px; top: 1136px;
    font-size: 18px;
    font-style: italic;
    letter-spacing: 0.3px;
  }
</style>
</head>
<body>
<div class="page">
  <aside class="sidebar">
    <div class="sidebar-photo" role="img" aria-label="Photo of schoolchildren in blue uniforms seated on the floor of a classroom with a blackboard"></div>
    <blockquote class="pull-quote">
      <span class="line">“This was a great</span>
      <span class="line">project, it helped</span>
      <span class="line">me understand</span>
      <span class="line">much more about</span>
      <span class="line">technology and</span>
      <span class="line">communicating</span>
      <span class="line">with others”</span>
    </blockquote>
  </aside>

  <header class="page-header">
    <h1 class="page-title">Notable indicator 2:</h1>
    <p class="page-subtitle">Enhancing courses through service-learning</p>
  </header>

  <main class="main-column">
    <h2 class="section-heading">
      <span class="line">Department activity: “Evidence of revision of</span>
      <span class="line">existing courses that significantly improve them”</span>
      <span class="line">(outstanding).</span>
    </h2>
    <p class="body-text">
      <span class="line">Service learning is the most important pedagogical concept</span>
      <span class="line">that I have embraced since starting at Blue Ridge State</span>
      <span class="line">University. I was introduced to service learning through the</span>
      <span class="line">Campus and Community Together (CCT) office here</span>
      <span class="line">on campus, and was selected as a cct faculty fellow for</span>
      <span class="line">the 2009 2010 academic year. Faculty fellows in service</span>
      <span class="line">learning attend a series of workshops on aspects of this</span>
      <span class="line">pedagogical model, and develop syllabi, or enhancing</span>
      <span class="line">existing syllabus, to integrate service learning activities into</span>
      <span class="line">a course.</span>
    </p>
    <p class="body-text">
      <span class="line">In preparation of the international service learning project,</span>
      <span class="line">I wrote a grant proposal for the strategic uses</span>
      <span class="line">of learning technologies (sult) grant offered by the Hartwell</span>
      <span class="line">College of Education for the academic year 2010 2011.</span>
      <span class="line">The application I spent on the idea of internationalizing</span>
      <span class="line">the web design course through an international service</span>
      <span class="line">learning project with partner organizations in the southern</span>
      <span class="line">state of Tamil Nadu, Indian. The International Office here</span>
      <span class="line">Blue Ridge State connected me with community partners</span>
      <span class="line">in the cities of Chennai and monitor I, whom I contacted</span>
      <span class="line">about the project ideas. Grant was successfully funded,</span>
      <span class="line">allowing me to travel to Chennai and Madurai to meet</span>
      <span class="line">with the partners and to expand on the project ideas that</span>
      <span class="line">students will be engaged in for the spring semester 2011.</span>
    </p>
  </main>

  <footer class="page-footer">CHAPTER 1, PAGE 1</footer>
</div>
</body>
</html>
```